Corrigan & Hale, LLC
Business Cards & Stationery
Corrigan & Hale, LLC -
Creative Brief
Professional
Deborah L. Corrigan
Attorney At Law
418 W. Brookfield Avenue Suite 3B Pearl River, New York 10965-2274
dcorrigan@corriganandhale-example.com
www.corriganandhale-example.com
We will need to be able to use template for other people in the firm.
Specializing in Civil Litigation, Wills, Trusts & Estates, Guardianships, and related matters

```html
<!DOCTYPE html>
<html lang="en">
<head>
<meta charset="utf-8">
<title>Corrigan &amp; Hale, LLC — Stationery</title>
<link href="https://fonts.googleapis.com/css2?family=Lato:wght@400;700&display=swap" rel="stylesheet">
<style>
:root{
  --bg:#2b2b2b;
  --paper:#ffffff;
  --green:#1d6a4a;
  --grey:#8a8d8f;
  --grey-light:#d4d6d7;
  --faint:#e3e9e6;
  --label:#9a9a9a;
  --ink:#3a3a3a;
}
*{margin:0;padding:0;box-sizing:border-box}
html,body{width:1200px;height:338px;overflow:hidden;background:var(--bg);font-family:"Lato",sans-serif}
.board{position:relative;width:1200px;height:338px}
.item{position:absolute;background:var(--paper);overflow:hidden}
.item svg.art{position:absolute;inset:0;width:100%;height:100%}
.label{position:absolute;font-size:5px;color:var(--label);letter-spacing:.3px;white-space:nowrap}
.brand{position:absolute;color:var(--green);font-weight:700;white-space:nowrap}
.brand.light{color:#fff}
.small{position:absolute;font-size:3px;color:var(--ink);line-height:1.4;white-space:nowrap}
.faint-name{position:absolute;color:var(--faint);font-weight:700;white-space:nowrap;text-align:center}

.card-front{left:12px;top:120px;width:96px;height:55px}
.card-back{left:12px;top:186px;width:96px;height:55px}
.letter-one{left:132px;top:24px;width:240px;height:300px}
.letter-two{left:396px;top:24px;width:240px;height:300px}
.env-front{left:660px;top:43px;width:240px;height:112px}
.env-window{left:660px;top:175px;width:240px;height:112px}
.env-back{left:912px;top:24px;width:276px;height:140px}
.env-back-alt{left:912px;top:180px;width:276px;height:132px}
</style>
</head>
<body>
<main class="board">

  <section class="item card-front">
    <svg class="art" viewBox="0 0 96 55" preserveAspectRatio="none" aria-hidden="true">
      <path d="M0 44 Q40 34 96 46 L96 55 L0 55Z" fill="var(--grey-light)"/>
      <path d="M0 48 Q45 40 96 51 L96 55 L0 55Z" fill="var(--green)"/>
    </svg>
    <div class="brand" style="left:6px;top:7px;font-size:4px">Corrigan &amp; Hale, LLC</div>
    <div class="small" style="left:6px;top:16px;font-weight:700;font-size:3.4px">Deborah L. Corrigan</div>
    <div class="small" style="left:6px;top:21px">Attorney At Law</div>
    <div class="small" style="left:6px;top:27px">418 W. Brookfield Avenue Suite 3B<br>dcorrigan@corriganandhale-example.com</div>
  </section>
  <div class="label" style="left:12px;top:178px">Business Card Front</div>

  <section class="item card-back" style="background:var(--green)">
    <svg class="art" viewBox="0 0 96 55" preserveAspectRatio="none" aria-hidden="true">
      <path d="M0 40 Q45 30 96 42 L96 55 L0 55Z" fill="var(--paper)"/>
      <path d="M0 44 Q45 36 96 47 L96 55 L0 55Z" fill="var(--grey-light)"/>
    </svg>
    <div class="brand light" style="left:0;right:0;top:16px;font-size:4.5px;text-align:center">Corrigan &amp; Hale</div>
  </section>
  <div class="label" style="left:12px;top:244px">Business Card Back</div>

  <section class="item letter-one">
    <svg class="art" viewBox="0 0 240 300" preserveAspectRatio="none" aria-hidden="true">
      <path d="M150 0 Q200 4 240 30 L240 0Z" fill="var(--green)"/>
      <path d="M0 262 Q120 230 240 250 L240 256 Q120 240 0 270Z" fill="var(--grey)"/>
      <path d="M0 270 Q110 244 240 256 L240 300 L0 300Z" fill="var(--green)"/>
    </svg>
    <div class="brand" style="left:16px;top:14px;font-size:5px">Corrigan &amp; Hale, LLC</div>
    <div class="small" style="left:16px;top:22px">Attorney At Law · Pearl River, New York</div>
  </section>
  <div class="label" style="left:132px;top:327px">Letterhead Page One</div>

  <section class="item letter-two">
    <svg class="art" viewBox="0 0 240 300" preserveAspectRatio="none" aria-hidden="true">
      <path d="M150 0 Q200 4 240 30 L240 0Z" fill="var(--green)"/>
      <path d="M0 262 Q120 230 240 250 L240 256 Q120 240 0 270Z" fill="var(--grey)"/>
      <path d="M0 270 Q110 244 240 256 L240 300 L0 300Z" fill="var(--green)"/>
    </svg>
    <div class="faint-name" style="left:0;right:0;top:130px;font-size:16px">Corrigan &amp; Hale</div>
  </section>
  <div class="label" style="left:396px;top:327px">Letterhead Page Two</div>

  <section class="item env-front">
    <svg class="art" viewBox="0 0 240 112" preserveAspectRatio="none" aria-hidden="true">
      <path d="M0 40 Q40 10 240 12 L240 26 Q60 24 0 48Z" fill="var(--grey)"/>
      <path d="M0 0 L120 0 Q40 12 0 36Z" fill="var(--green)"/>
    </svg>
    <div class="brand" style="left:130px;top:3px;font-size:4.5px">Corrigan &amp; Hale, LLC</div>
  </section>
  <div class="label" style="left:660px;top:158px">Envelope Front</div>

  <section class="item env-window">
    <svg class="art" viewBox="0 0 240 112" preserveAspectRatio="none" aria-hidden="true">
      <path d="M0 0 L240 0 L240 12 Q120 4 0 24Z" fill="var(--green)"/>
      <path d="M0 24 Q120 4 240 12 L240 16 Q120 10 0 30Z" fill="var(--grey)"/>
    </svg>
    <div class="brand light" style="left:8px;top:3px;font-size:4px">Corrigan &amp; Hale, LLC</div>
    <div class="faint-name" style="left:150px;top:72px;font-size:8px">Corrigan &amp; Hale</div>
  </section>
  <div class="label" style="left:660px;top:290px">Envelope Window</div>

  <section class="item env-back">
    <svg class="art" viewBox="0 0 276 140" preserveAspectRatio="none" aria-hidden="true">
      <path d="M0 0 L276 0 L276 20 L138 70 L0 20Z" fill="var(--green)"/>
      <path d="M0 140 L138 72 L276 140" fill="none" stroke="var(--grey-light)" stroke-width="1"/>
    </svg>
    <div class="brand light" style="left:0;right:0;top:40px;font-size:4.5px;text-align:center">Corrigan &amp; Hale</div>
  </section>
  <div class="label" style="left:912px;top:167px">Envelope Back</div>

  <section class="item env-back-alt">
    <svg class="art" viewBox="0 0 276 132" preserveAspectRatio="none" aria-hidden="true">
      <path d="M0 0 L276 0 L276 20 L138 66 L0 20Z" fill="var(--grey-light)"/>
      <path d="M0 132 L138 68 L276 132" fill="none" stroke="var(--grey-light)" stroke-width="1"/>
    </svg>
  </section>
  <div class="label" style="left:1080px;top:315px">Envelope Back Alt</div>

</main>
</body>
</html>
```